Innovative, creative, and beautiful simple book cover!

I’ve spend 5 years writing a book about executive consulting. Last task of the project is to find the best possible cover and I need help from you guys.

In the book, I take the liberty of creating a model which secures successful sales throughout the value chain, driven by the top management.

For you info, I used Pixel Harbor once before and of cause ended buying a logo. In short I’m here to buy the best book cover idea - and look forward to see what genius ideas you can bring to the table.

Thank you very much.
Torvald

P.S. Please see my brief in attach documents. .
Updates

Target Market(s)

Business people en general

Industry/Entity Type

Management Consulting

Font styles to use
Sans Serif

Requirements
Must have
• - My attach files about description for front page and back page have to be incorporated.
• - BOTH A FRONT, SPINE AND A BACK PAGE!
• - Please see all my attach files – the project is very well described and should be ready to work on.
• - The idea about the “building line” is an idea I love, but if you have something else you think I should see – try me.
Nice to have
• I love simple, minimalistic design
Should not have
• I don't like old fashion or over designed solutions. Sorry :-)

```html
<!DOCTYPE html>
<html lang="en">
<head>
<meta charset="utf-8">
<title>Executive Sales Efficiency – Spine and Front Cover</title>
<link rel="stylesheet" href="https://fonts.googleapis.com/css2?family=Playfair+Display:wght@900&family=Libre+Baskerville:ital,wght@0,400;1,700&display=swap">
<style>
  :root {
    --backdrop: #7a9cab;
    --backdrop-deep: #557c8e;
    --paper: #f1f2f4;
    --paper-line: #e6e8eb;
    --navy: #0f2a5c;
    --slate: #3d5275;
    --slate-light: #8696b0;
    --amber: #e08a2c;
    --sand: #efb27a;
    --spine-ink: #c9ced8;
    --white: #ffffff;
  }
  * { box-sizing: border-box; margin: 0; padding: 0; }
  html, body {
    width: 1200px;
    height: 784px;
    overflow: hidden;
  }
  body {
    background: radial-gradient(ellipse at 45% 35%, var(--backdrop) 0%, var(--backdrop-deep) 100%);
    position: relative;
  }
  .book {
    position: absolute;
    left: 352px;
    top: 72px;
    height: 640px;
    display: flex;
    box-shadow: 0 18px 40px rgba(20, 40, 60, 0.35);
  }
  .spine {
    width: 56px;
    height: 100%;
    background: var(--navy);
    display: flex;
    align-items: center;
    justify-content: center;
  }
  .spine-title {
    writing-mode: vertical-rl;
    font-family: "Libre Baskerville", serif;
    font-size: 17px;
    letter-spacing: 1px;
    color: var(--spine-ink);
    white-space: nowrap;
  }
  .cover {
    position: relative;
    width: 440px;
    height: 100%;
    background: repeating-linear-gradient(90deg, var(--paper) 0 2px, var(--paper-line) 2px 3px);
    text-align: center;
    font-family: "Playfair Display", serif;
  }
  .title-line {
    position: absolute;
    left: 0;
    width: 100%;
    font-weight: 900;
    text-transform: uppercase;
    line-height: 1;
    white-space: nowrap;
  }
  .title-top,
  .title-bottom {
    font-size: 44px;
    background: repeating-linear-gradient(135deg, var(--slate) 0 1.5px, var(--slate-light) 1.5px 3px);
    -webkit-background-clip: text;
    background-clip: text;
    color: transparent;
    -webkit-text-stroke: 1px var(--navy);
  }
  .title-top { top: 124px; }
  .title-bottom { top: 266px; }
  .title-band {
    position: absolute;
    left: 0;
    top: 176px;
    width: 100%;
    height: 80px;
    background: var(--navy);
  }
  .title-main {
    top: 176px;
    font-size: 76px;
    line-height: 80px;
    background: repeating-linear-gradient(135deg, var(--white) 0 2px, var(--slate-light) 2px 3px);
    -webkit-background-clip: text;
    background-clip: text;
    color: transparent;
    -webkit-text-stroke: 1px var(--white);
  }
  .byline {
    position: absolute;
    top: 348px;
    left: 0;
    width: 100%;
    font-family: "Libre Baskerville", serif;
  }
  .byline-label {
    display: inline-flex;
    align-items: center;
    gap: 6px;
    font-size: 8px;
    font-style: italic;
    font-weight: 700;
    letter-spacing: 0.5px;
    color: var(--amber);
  }
  .byline-label::before,
  .byline-label::after {
    content: "";
    width: 40px;
    height: 1px;
    background: var(--navy);
  }
  .author {
    margin-top: 4px;
    font-size: 17px;
    color: var(--navy);
  }
  .skyline {
    position: absolute;
    left: 22px;
    right: 22px;
    bottom: 48px;
    height: 170px;
  }
</style>
</head>
<body>
  <div class="book">
    <aside class="spine">
      <p class="spine-title">EXECUTIVE SALES EFFICIENCY</p>
    </aside>
    <main class="cover">
      <h1>
        <span class="title-line title-top">Executive</span>
        <span class="title-band" aria-hidden="true"></span>
        <span class="title-line title-main">Sales</span>
        <span class="title-line title-bottom">Efficiency</span>
      </h1>
      <div class="byline">
        <p class="byline-label">WRITTEN BY</p>
        <p class="author">TORVALD LINDQVIST</p>
      </div>
      <svg class="skyline" viewBox="0 0 396 170" role="img" aria-label="City skyline illustration with landmark towers in amber above a navy striped ground">
        <defs>
          <linearGradient id="skylineFill" x1="0" y1="0" x2="0" y2="1">
            <stop offset="0" stop-color="var(--paper)"/>
            <stop offset="0.25" stop-color="var(--sand)"/>
            <stop offset="0.6" stop-color="var(--sand)"/>
            <stop offset="0.75" stop-color="var(--slate)"/>
            <stop offset="1" stop-color="var(--navy)"/>
          </linearGradient>
        </defs>
        <rect x="0" y="0" width="396" height="170" fill="url(#skylineFill)"/>
      </svg>
    </main>
  </div>
</body>
</html>
```